Poster/Flyer design for a Church Youth Group Event

We need a flyer for Pathway Rally 2013. This event is being put on by 6 different churches. The event is for youth from 6th grade to 12th grade. The theme for this event is "Walk In Trust" this is taken from Hebrews 11:1-39.
This flyer will be put up in both schools and the churches. It will also be included with the registration forms for the event.

Target Market(s)

Youth - Ages 11-18

Industry/Entity Type

Church

Requirements
Must have
• We would like the phrases "Walk In Trust" and "Pathway Rally 2013" to be the focal point of the flyer. We would also like the the verse "Hebrews 11:1-39" on the flyer as well.
The date for the event - Feb. 6, 8-10
Cost - $25
There is some additional information that needs to be on the flyer as well:
Speaker - Dr. Marcus Dunbar
Worship Leader - Sam Okafor
I've included pictures of the speaker and the worship leader. It would be nice to have the pics on the flyer, but it is not essential.

We need the names of the churches involved: FBC Cedar Hollow, Marlow Methodist, FBC Marlow, Briar Baptist, Sable Creek Valley C of C, & Cedar Hollow C of C. It doesn't really matter where or how these are on the design, as long as it is there

The flyer also needs to say "registration forms can be picked up in the office or from one of the churches"

I have included a picture of the t-shirt for the event. A similar design style would be great.

```html
<!DOCTYPE html>
<html lang="en">
<head>
<meta charset="utf-8">
<title>Pathway Rally 2013 – Walk In Trust</title>
<link rel="stylesheet" href="https://fonts.googleapis.com/css2?family=Dancing+Script:wght@700&family=Tinos:ital,wght@0,700;1,700&family=Source+Sans+3:wght@600;700&display=swap">
<style>
  :root {
    --navy: #1d2c5e;
    --sky-deep: #3f74cf;
    --sky-mid: #5b8fe0;
    --sky-light: #a9c8f3;
    --white: #ffffff;
    --band: rgba(255, 255, 255, 0.45);
    --photo-frame: #2f3f8a;
  }
  * { margin: 0; padding: 0; box-sizing: border-box; }
  html, body { width: 776px; height: 1200px; overflow: hidden; }
  body { background: var(--sky-deep); }
  .flyer {
    position: relative;
    width: 776px;
    height: 1200px;
    overflow: hidden;
    background:
      radial-gradient(ellipse 360px 300px at 600px 820px, rgba(190,215,250,0.75), transparent 70%),
      radial-gradient(ellipse 300px 360px at 360px 120px, rgba(200,222,252,0.7), transparent 70%),
      linear-gradient(180deg, var(--sky-mid) 0%, var(--sky-deep) 45%, var(--sky-mid) 100%);
    font-family: "Tinos", "Times New Roman", serif;
    color: var(--navy);
  }
  .backdrop-flowers {
    position: absolute; left: 330px; top: 520px; width: 446px; height: 560px;
    background: radial-gradient(ellipse at 60% 55%, rgba(210,228,255,0.55), rgba(120,160,230,0.15) 60%, transparent 80%);
  }
  .year-watermark {
    position: absolute; font-family: "Source Sans 3", sans-serif; font-weight: 700;
    color: rgba(255,255,255,0.10); line-height: 1;
  }
  .year-watermark.top { right: -40px; top: 20px; font-size: 520px; }
  .year-watermark.bottom { left: 40px; top: 620px; font-size: 480px; }
  .headline {
    position: absolute; top: 22px; width: 100%; text-align: center;
    font-family: "Dancing Script", cursive; font-size: 50px; color: var(--navy);
  }
  .invite {
    position: absolute; top: 100px; width: 100%; text-align: center;
    font-size: 33px; color: var(--white);
  }
  .photo {
    position: absolute; border: 3px solid var(--photo-frame);
    box-shadow: 0 4px 10px rgba(0,0,0,0.25);
  }
  .photo.speaker {
    left: 22px; top: 168px; width: 262px; height: 264px; transform: rotate(-4deg);
    background: linear-gradient(160deg, #5b3fa3, #3b2a7a 60%, #2a2d55);
  }
  .photo.worship {
    left: 38px; top: 440px; width: 300px; height: 296px; transform: rotate(6deg);
    background: linear-gradient(150deg, #d98a6e, #b96a5a 45%, #6b5550);
  }
  .event-name {
    position: absolute; top: 200px; left: 512px; width: 260px; text-align: center;
    font-family: "Source Sans 3", sans-serif; font-weight: 600; font-size: 32px;
    line-height: 1.45; color: var(--white);
  }
  .theme {
    position: absolute; left: 256px; top: 250px;
    font-family: "Dancing Script", cursive; color: var(--navy); white-space: nowrap;
  }
  .theme .initial { font-size: 200px; line-height: 1; vertical-align: top; }
  .theme .rest { font-size: 64px; position: relative; top: 62px; left: -8px; }
  .date-pill {
    position: absolute; left: 372px; top: 486px; width: 420px; height: 104px;
    background: var(--white); border-radius: 24px 0 0 24px;
    display: flex; flex-direction: column; justify-content: center;
    padding-left: 42px;
    font-family: "Source Sans 3", sans-serif; font-weight: 700; font-size: 36px;
    line-height: 1.15; color: var(--navy);
  }
  .verse {
    position: absolute; top: 628px; left: 430px; width: 320px; text-align: center;
    font-size: 29px; color: var(--white);
  }
  .cost {
    position: absolute; top: 688px; left: 430px; width: 290px; text-align: center;
    font-size: 29px; color: var(--navy);
  }
  .leaders-band {
    position: absolute; top: 762px; left: 0; width: 100%; height: 64px;
    background: var(--band); display: flex; align-items: center;
    font-size: 22px; color: var(--navy);
  }
  .leaders-band .leader { flex: 1; text-align: center; }
  .leaders-band .leader.first { flex: 0 0 384px; padding-left: 10px; }
  .leaders-band .divider { width: 4px; height: 40px; background: var(--navy); }
  .churches {
    position: absolute; top: 852px; width: 100%; text-align: center;
    font-size: 22px; line-height: 1.4; color: var(--navy);
  }
  .registration {
    position: absolute; top: 980px; left: 22px;
    font-style: italic; font-size: 23px; line-height: 1.4; color: var(--navy);
  }
  .registration .mark { font-style: normal; font-size: 30px; margin-right: 6px; }
  .registration .indent { padding-left: 26px; }
  .tshirt {
    position: absolute; top: 1054px; width: 190px; height: 118px;
    background: linear-gradient(180deg, #4a86d8, #2f63b8);
  }
  .tshirt.left { left: 0; }
  .tshirt.right { right: 0; }
  .tshirt-caption {
    position: absolute; top: 1156px; width: 100%; text-align: center;
    font-size: 22px; color: var(--navy);
  }
</style>
</head>
<body>
<main class="flyer">
  <div class="backdrop-flowers" role="img" aria-label="Soft blue flower petals in the background"></div>
  <div class="year-watermark top">20</div>
  <div class="year-watermark bottom">13</div>

  <h1 class="headline">Are you a Youth aged 11 to 18?</h1>
  <p class="invite">Come and Enjoy with us</p>

  <div class="photo speaker" role="img" aria-label="Portrait photo of speaker Dr. Marcus Dunbar"></div>
  <div class="photo worship" role="img" aria-label="Photo of worship leader Sam Okafor playing music"></div>

  <p class="event-name">Pathway Rally<br>2013</p>
  <h2 class="theme"><span class="initial">W</span><span class="rest">alk In Trust</span></h2>

  <div class="date-pill"><span>6TH, 8TH - 10TH</span><span>FEBRUARY 2013</span></div>

  <p class="verse">Hebrews 11:1-39</p>
  <p class="cost">Cost: $25</p>

  <div class="leaders-band">
    <span class="leader first">Speaker - Dr. Marcus Dunbar</span>
    <span class="divider"></span>
    <span class="leader">Worship Leader - Sam Okafor</span>
  </div>

  <p class="churches">Churches:<br>FBC Cedar Hollow, Marlow Methodist, FBC Marlow,<br>Briar Baptist, Sable Creek Valley C of C, &amp; Cedar Hollow C of C</p>

  <p class="registration"><span class="mark">*</span>Registration forms can be picked up in the office<br><span class="indent">or from one of the churches.</span></p>

  <div class="tshirt left" role="img" aria-label="Blue event t-shirt, front view"></div>
  <div class="tshirt right" role="img" aria-label="Blue event t-shirt, back view"></div>
  <p class="tshirt-caption">T-shirt for the event</p>
</main>
</body>
</html>
```